Brand New Luxury Dog Kennel Needs a Flyer Design

We need a flyer design for a new type of dog kennel in Derbyshire (UK). We are trying to separate ourselves from the original kennel types and offer a more hotel orientated approach with much better facilities, massive rooms, large play areas (indoors and out (across the farm land)), 24/7 web cam access for the owners, etc.
The name of the company is Cat and Ladle, it's based on a farm called Brambleton Farm.
We have started a website (not complete yet), but you can get an idea of style there; http://www.catandladle-example.co.uk/
The final design should emphasise that we are different from the other kennels, we're very professional and caring. It's very much the dogs holiday.
Size of Flyer should be around 216 x 139 mm

```html
<!DOCTYPE html>
<html lang="en">
<head>
<meta charset="utf-8">
<title>Cat and Ladle – Flyer</title>
<link rel="stylesheet" href="https://fonts.googleapis.com/css2?family=Josefin+Sans:wght@300;400&family=Dancing+Script:wght@700&display=swap">
<style>
  :root {
    --page-bg: #2b2b2b;
    --brown-light: #6a3a22;
    --brown-dark: #341b11;
    --green: #4a9a1f;
    --green-light: #6cc22e;
    --silver: #e4e4e4;
    --label-bg: #f3f0ea;
    --ink: #3a2418;
    --tagline: #4a4a4a;
    --white: #ffffff;
  }
  * { margin: 0; padding: 0; box-sizing: border-box; }
  html, body { width: 959px; height: 1200px; overflow: hidden; }
  body { background: var(--page-bg); position: relative; font-family: "Josefin Sans", sans-serif; }

  .flyer {
    position: absolute; left: 57px; top: 60px;
    width: 844px; height: 1085px; overflow: hidden;
    background: radial-gradient(ellipse at 50% 60%, var(--brown-light) 0%, var(--brown-dark) 85%);
  }
  .flyer__photo {
    position: absolute; left: 0; top: 0; width: 844px; height: 420px;
    background: linear-gradient(100deg, #b8742e 0%, #c98c3e 25%, #e7cf5a 55%, #d9d46a 75%, #8fae48 100%);
  }
  .flyer__shapes { position: absolute; left: 0; top: 0; width: 844px; height: 1085px; }

  .label {
    position: absolute; left: 246px; top: 468px; width: 355px; height: 242px;
    background: var(--label-bg);
    clip-path: polygon(0 0, 100% 0, 100% 100%, 50% 88%, 0 100%);
    text-align: center;
  }
  .label__name {
    margin-top: 88px;
    font-family: "Josefin Sans", sans-serif; font-weight: 400;
    font-size: 36px; color: var(--ink);
  }
  .label__tagline {
    margin-top: 22px;
    font-size: 19px; font-weight: 300; color: var(--tagline);
  }

  .flyer__intro {
    position: absolute; left: 40px; top: 733px; width: 764px;
    text-align: center; color: var(--white);
    font-size: 19px; font-weight: 300; line-height: 30px;
  }
  .flyer__headline {
    position: absolute; left: 0; top: 868px; width: 844px;
    text-align: center; color: var(--white);
    font-family: "Dancing Script", cursive; font-weight: 700; font-size: 54px;
  }
  .flyer__web {
    position: absolute; left: 0; top: 1014px; width: 844px;
    text-align: center; color: var(--white);
    font-size: 31px; font-weight: 300;
  }
</style>
</head>
<body>
  <main class="flyer">
    <div class="flyer__photo" role="img" aria-label="Photo of a happy sable-and-white collie in front of sunlit autumn foliage"></div>

    <svg class="flyer__shapes" viewBox="0 0 844 1085" aria-hidden="true">
      <defs>
        <linearGradient id="greenSwoosh" x1="0" y1="0" x2="1" y2="0">
          <stop offset="0" stop-color="var(--green)"/>
          <stop offset="1" stop-color="var(--green-light)"/>
        </linearGradient>
      </defs>
      <!-- top swoosh -->
      <path d="M0,362 Q330,450 844,200 L844,385 Q422,485 0,390 Z" fill="url(#greenSwoosh)"/>
      <path d="M0,390 Q422,485 844,385 L844,420 Q422,500 0,420 Z" fill="var(--brown-dark)"/>
      <path d="M0,392 Q422,487 844,386" fill="none" stroke="var(--silver)" stroke-width="9"/>
      <!-- bottom band -->
      <path d="M0,1002 Q422,948 844,1002 L844,1085 L0,1085 Z" fill="url(#greenSwoosh)"/>
      <path d="M0,998 Q422,944 844,998" fill="none" stroke="var(--silver)" stroke-width="9"/>
    </svg>

    <div class="label">
      <p class="label__name">Cat and Ladle</p>
      <p class="label__tagline">The dog hotel with a difference</p>
    </div>

    <p class="flyer__intro">The Cat and Ladle was specifically designed and built with the concept of quality over quantity; our 6 spacious rooms, indoor play area, outdoor agility park, 24/7 web cam access for the ownersand secured exercise fields is testimony to that. Come and have a visit.</p>

    <h1 class="flyer__headline">Its very much the dogs holiday</h1>

    <p class="flyer__web">www.catandladle-example.co.uk</p>
  </main>
</body>
</html>
```